Modern Academic Informational Postcard and Graphic

I am looking for a postcard design, with a fast turnaround time (24-hours). These postcards will be handed out at a presentation that is being given as part of an interview process. I would like to print two information cards per 8.5/11 piece of paper. These cards will be double sided. The front side is a visual graphic representing the 4 elements of the vision this interview candidate plans to bring to the position. The backside includes a snapshot of this candidate’s academic and administrative background. I have attached a sketch of the front and back sides. There should also be a simple visual on the backside denoting a spot reserved for Marlowe College (MC) on this career continuum (on the sketch this is represented by a star with MC in the middle).

I would like the crimson palatte to be used (https://www.marlowecollege-example.org/brand/design/color.html) and, if possible Benton Sans font. And the overall aesthetic should be modern and minimalistic, and convey professionalism. The information does not have to be presented in the way that it is in the attached documents (this was just a rough sketch/idea).

```html
<!DOCTYPE html>
<html lang="en">
<head>
<meta charset="utf-8">
<title>Inspire Impact – Candidate Postcard</title>
<link href="https://fonts.googleapis.com/css2?family=Open+Sans:wght@400;600;700&display=swap" rel="stylesheet">
<style>
  :root {
    --crimson: #990000;
    --white: #ffffff;
    --page: #f3f3f3;
  }
  * { box-sizing: border-box; margin: 0; padding: 0; }
  html, body {
    width: 1200px; height: 848px; overflow: hidden;
    background: var(--page);
    font-family: "Open Sans", Arial, sans-serif;
  }
  .card {
    position: absolute; top: 208px;
    width: 560px; height: 432px;
    background: var(--white);
  }
  .card--back { left: 30px; }
  .card--front { left: 610px; }

  /* Back side */
  .sidebar {
    position: absolute; left: 0; top: 0; width: 160px; height: 100%;
    background: var(--crimson); color: var(--white); overflow: hidden;
  }
  .sidebar__name { position: absolute; left: 30px; top: 55px; font-size: 14px; font-weight: 600; letter-spacing: .2px; white-space: nowrap; }
  .sidebar__pronoun { position: absolute; left: 29px; top: 78px; font-size: 10px; }
  .sidebar__dash { position: absolute; left: 30px; top: 248px; width: 14px; height: 4px; background: var(--white); }
  .sidebar__title { position: absolute; left: 30px; top: 258px; font-size: 13px; line-height: 18px; }
  .sidebar__email { position: absolute; left: 30px; top: 382px; font-size: 11px; white-space: nowrap; }

  .section-head {
    position: absolute; left: 185px; width: 355px;
    color: var(--crimson); font-size: 13px; font-weight: 400;
    border-bottom: 2px solid var(--crimson); padding-bottom: 1px;
  }
  .entry { position: absolute; left: 185px; width: 355px; height: 38px; display: flex; }
  .entry__role {
    flex: 0 0 168px; height: 38px; background: var(--crimson); color: var(--white);
    padding: 5px 9px; font-size: 10px; line-height: 14px;
  }
  .entry__role strong { font-weight: 700; display: block; white-space: nowrap; }
  .entry__place { padding: 5px 0 0 11px; color: var(--crimson); font-size: 9.5px; line-height: 15px; white-space: nowrap; }

  .continuum { position: absolute; left: 185px; top: 193px; width: 355px; height: 36px; }
  .continuum__line { position: absolute; left: 0; top: 16px; width: 290px; height: 2px; background: var(--crimson); }
  .continuum__name { position: absolute; right: 36px; top: 8px; color: var(--crimson); font-size: 13px; font-weight: 700; }
  .continuum__mark { position: absolute; right: 0; top: 2px; width: 31px; height: 31px; background: var(--crimson); }

  /* Front side */
  .front__band { position: absolute; left: 0; top: 0; width: 23px; height: 100%; background: var(--crimson); }
  .wheel { position: absolute; left: 0; top: 0; }
  .pillar { font-family: "Open Sans", Arial, sans-serif; font-size: 14px; font-weight: 600; fill: var(--crimson); }
  .hub { font-family: "Open Sans", Arial, sans-serif; font-size: 22px; font-weight: 700; fill: var(--white); }
</style>
</head>
<body>

<section class="card card--back" aria-label="Academic and administrative background">
  <aside class="sidebar">
    <div class="sidebar__name">DANA C. LEE</div>
    <div class="sidebar__pronoun">(she/her)</div>
    <div class="sidebar__dash"></div>
    <div class="sidebar__title">Academic &amp;<br>Administrative<br>Background</div>
    <div class="sidebar__email">dlee@pst.example</div>
  </aside>

  <h2 class="section-head" style="top:55px;">Education</h2>
  <div class="entry" style="top:90px;">
    <div class="entry__role"><strong>Teacher</strong>1998-2000</div>
    <div class="entry__place">Elmwood Middle School<br>Cedar Valley ISD, Riverton</div>
  </div>
  <div class="entry" style="top:139px;">
    <div class="entry__role"><strong>Professor</strong>2004 - present</div>
    <div class="entry__place">Educational Leadership &amp; Policy Studies<br>Prairie State University</div>
  </div>

  <div class="continuum">
    <div class="continuum__line"></div>
    <span class="continuum__name">MC</span>
    <div class="continuum__mark"></div>
  </div>

  <h2 class="section-head" style="top:236px;">University</h2>
  <div class="entry" style="top:271px;">
    <div class="entry__role"><strong>Director of Academic Inclusion</strong>2018-2019</div>
    <div class="entry__place">Office of Diversity &amp; Equity<br>Prairie State University</div>
  </div>
  <div class="entry" style="top:320px;">
    <div class="entry__role"><strong>Interim Vice Provost</strong>2019-2021</div>
    <div class="entry__place">Office of Diversity &amp; Equity<br>Prairie State University</div>
  </div>
  <div class="entry" style="top:370px;">
    <div class="entry__role"><strong>Associate Vice Provost</strong>2021-2023</div>
    <div class="entry__place">Office of Faculty Affairs<br>Prairie State University</div>
  </div>
</section>

<section class="card card--front" aria-label="Inspire Impact vision">
  <div class="front__band"></div>
  <svg class="wheel" width="560" height="432" viewBox="0 0 560 432">
    <g transform="translate(280 217)">
      <circle r="126" fill="#990000"/>
      <rect x="-4.5" y="-130" width="9" height="260" fill="#fff"/>
      <rect x="-130" y="-4.5" width="260" height="9" fill="#fff"/>
      <circle r="67" fill="#fff"/>
      <circle r="58" fill="#990000"/>
      <text class="hub" text-anchor="middle" y="-4">INSPIRE</text>
      <text class="hub" text-anchor="middle" y="21">IMPACT</text>

      <g fill="#fff">
        <circle cx="-89" cy="-89" r="13"/><circle cx="89" cy="-89" r="13"/>
        <circle cx="-89" cy="89" r="13"/><circle cx="89" cy="89" r="13"/>
      </g>
      <g fill="#990000">
        <circle cx="-89" cy="-89" r="8"/><circle cx="89" cy="-89" r="8"/>
        <circle cx="-89" cy="89" r="8"/><circle cx="89" cy="89" r="8"/>
      </g>

      <g fill="#fff" stroke="#fff">
        <g transform="translate(30 -97)">
          <circle r="11" fill="none" stroke-width="6" stroke-dasharray="4 3"/>
          <circle r="7" stroke="none"/>
        </g>
        <g transform="translate(-91 -31)" stroke="none">
          <circle cy="-3" r="5"/>
          <rect x="-8" y="4" width="16" height="8" rx="3"/>
          <circle cx="-11" cy="-10" r="1.6"/><circle cx="0" cy="-15" r="1.6"/><circle cx="11" cy="-10" r="1.6"/>
        </g>
        <g transform="translate(91 31)" stroke="none">
          <rect x="-7" y="-16" width="12" height="8" rx="1"/>
          <circle cx="-9" cy="0" r="3.5"/><rect x="-14" y="5" width="10" height="7" rx="2"/>
          <circle cx="9" cy="0" r="3.5"/><rect x="4" y="5" width="10" height="7" rx="2"/>
        </g>
        <g transform="translate(-30 97)" stroke="none">
          <circle cy="-9" r="3.5"/><rect x="-4" y="-5" width="8" height="15" rx="2"/>
          <circle cx="-10" cy="-5" r="3"/><rect x="-13" y="-1" width="6" height="12" rx="2"/>
          <circle cx="10" cy="-5" r="3"/><rect x="7" y="-1" width="6" height="12" rx="2"/>
        </g>
      </g>
    </g>

    <text class="pillar" text-anchor="end" x="171" y="117">Student</text>
    <text class="pillar" text-anchor="end" x="171" y="133">Experiences</text>
    <text class="pillar" x="390" y="117">Organizational</text>
    <text class="pillar" x="390" y="133">Capacity</text>
    <text class="pillar" text-anchor="end" x="171" y="306">Outreach and</text>
    <text class="pillar" text-anchor="end" x="171" y="322">Leadership</text>
    <text class="pillar" x="389" y="306">Assessment and</text>
    <text class="pillar" x="389" y="322">Communications</text>
  </svg>
</section>

</body>
</html>
```